Atelier Mirou

I am actually making my own traditional french food.
Everything is homemade with passion.
I make differente terrines, jams, macaroons, rillettes and much more
I do as well cocktail party and catering

Hello everyone,

On the business card I would like to see appear if it's possible these following informations: traditional french food, cocktail party and catering.

```html
<!DOCTYPE html>
<html lang="en">
<head>
<meta charset="utf-8">
<title>Atelier Mirou — Business Card</title>
<link rel="stylesheet" href="https://fonts.googleapis.com/css2?family=Exo+2:wght@400;500;600&display=swap">
<style>
  :root {
    --page-bg: #ece9e4;
    --card-white: #ffffff;
    --card-red: #bf1e2e;
    --flag-blue: #2e3192;
    --flag-red: #c1272d;
    --ink: #1c1c1c;
    --light: #ffffff;
    --font: "Exo 2", sans-serif;
  }
  * { margin: 0; padding: 0; box-sizing: border-box; }
  html, body { width: 1200px; height: 841px; overflow: hidden; }
  body {
    background: var(--page-bg);
    font-family: var(--font);
    display: flex;
    align-items: center;
    justify-content: center;
    gap: 40px;
  }
  .card {
    position: relative;
    width: 540px;
    height: 309px;
    overflow: hidden;
    box-shadow: 0 6px 18px rgba(0,0,0,0.18);
  }
  .card-front { background: var(--card-white); }
  .card-back { background: var(--card-red); }

  .front-waves { position: absolute; inset: 0; width: 100%; height: 100%; }

  .brand {
    display: flex;
    align-items: center;
    gap: 10px;
    font-family: var(--font);
    font-weight: 600;
    text-transform: uppercase;
    letter-spacing: 0.08em;
    color: var(--ink);
  }
  .brand-dot {
    width: 16px; height: 16px;
    border-radius: 50%;
    background: var(--flag-red);
  }
  .card-front .brand {
    position: absolute;
    left: 28px; top: 54px;
    font-size: 24px;
  }

  .contact {
    position: absolute;
    right: 26px;
    top: 172px;
    color: var(--light);
    font-size: 12px;
    line-height: 15px;
    text-align: right;
  }
  .contact-name { font-weight: 500; }
  .contact-role { margin-bottom: 7px; }
  .contact-address { margin-bottom: 7px; }
  .contact-lines {
    display: grid;
    grid-template-columns: auto auto;
    column-gap: 10px;
    justify-content: end;
    text-align: left;
  }

  .card-back .brand {
    position: absolute;
    left: 50%; top: 108px;
    transform: translateX(-50%);
    font-size: 34px;
    white-space: nowrap;
  }
  .card-back .brand-dot { width: 22px; height: 22px; background: var(--light); }
  .tagline {
    position: absolute;
    left: 0; right: 0; top: 200px;
    text-align: center;
    color: var(--light);
    font-size: 14px;
    letter-spacing: 0.03em;
  }
</style>
</head>
<body>

  <section class="card card-front" aria-label="Business card front">
    <svg class="front-waves" viewBox="0 0 540 309" aria-hidden="true">
      <path d="M0,176 C140,146 250,170 370,154 C440,145 495,136 540,132 L540,309 L0,309 Z" fill="var(--flag-blue)"/>
      <path d="M0,186 C140,156 250,180 370,164 C440,155 495,146 540,142" fill="none" stroke="var(--light)" stroke-width="2"/>
      <path d="M200,152 C320,124 440,112 540,112 L540,126 C460,128 380,136 300,148 C260,154 230,155 200,152 Z" fill="var(--flag-red)"/>
    </svg>

    <div class="brand"><span class="brand-dot"></span>Atelier Mirou</div>

    <div class="contact">
      <p class="contact-name">Julien Castel</p>
      <p class="contact-role">Owner</p>
      <p class="contact-address">14 Rue Saint-Roch<br>Harbour Street 42</p>
      <div class="contact-lines">
        <span>Phone:</span><span>0412558731</span>
        <span>Email:</span><span>julien.castel@mail.fr</span>
        <span>ABN:</span><span>98765432101</span>
      </div>
    </div>
  </section>

  <section class="card card-back" aria-label="Business card back">
    <div class="brand"><span class="brand-dot"></span>Atelier Mirou</div>
    <p class="tagline">Traditional french food | Cocktail Party and Catering</p>
  </section>

</body>
</html>
```